Bottle label design for a mulberry brandy

Please create a label design for a mulberry brandy. The registered brand name is "Kolvat"
The brandy will be produced in Armenia from 100% mulberry.
Color of the product: transparent.
The product will be sold worldwide. The price will be between 30 and 50 USD. So the product will be in premium category.
Therefore we need a solid design, appropriate to the product price category. The design, however, needs to be modern and optimistic.
You can have mulberries on the label or not have, it is up to you.
We have chosen for the product some bottle types, the links to the available bottles you can find in the attachment. Ideally you show a picture of your label on the bottle you selected.

Target Market(s)

worldwide

```html
<!DOCTYPE html>
<html lang="en">
<head>
<meta charset="utf-8">
<title>Kolvat Mulberry Brandy Label</title>
<link rel="stylesheet" href="https://fonts.googleapis.com/css2?family=Federo&family=Oswald:wght@400;500&display=swap">
<style>
  :root {
    --backdrop: #cfcfcf;
    --label-paper: #f6f7f8;
    --marble-vein: #e3e6e9;
    --frame-grey: #a9a9a9;
    --frame-light: #d9d9d9;
    --brand-red: #d42a22;
    --band-grey: #5f5d5e;
    --band-text: #ffffff;
    --leaf-green: #3d8a3a;
    --berry-red: #b3202c;
  }
  * { margin: 0; padding: 0; box-sizing: border-box; }
  html, body {
    width: 1200px; height: 960px; overflow: hidden;
    background: radial-gradient(ellipse at 50% 40%, #e2e2e2 0%, var(--backdrop) 100%);
  }
  .label {
    position: absolute; left: 310px; top: 38px;
    width: 580px; height: 885px;
  }
  .label-frame { position: absolute; inset: 0; }
  .brand-row {
    position: absolute; left: 0; top: 222px; width: 580px; height: 110px;
  }
  .brand-name {
    position: absolute; left: 0; right: 0; top: 0;
    text-align: center;
    font-family: "Federo", sans-serif;
    font-size: 104px; line-height: 110px;
    color: var(--brand-red);
    letter-spacing: 2px;
  }
  .fruit-art {
    position: absolute; left: 140px; top: 380px; width: 350px; height: 330px;
    border-radius: 46% 54% 40% 60% / 50% 42% 58% 50%;
    background: radial-gradient(circle at 45% 42%, var(--berry-red) 0%, var(--berry-red) 22%, var(--leaf-green) 36%, #2f7430 70%, rgba(47,116,48,0) 72%);
  }
  .content-band {
    position: absolute; left: 70px; top: 715px; width: 443px; height: 68px;
    background: var(--band-grey);
    display: flex; align-items: center; justify-content: center;
  }
  .content-claim {
    font-family: "Oswald", sans-serif; font-weight: 400;
    font-size: 50px; line-height: 1;
    color: var(--band-text);
    transform: scaleX(0.82);
    white-space: nowrap;
  }
</style>
</head>
<body>
  <main class="label">
    <svg class="label-frame" viewBox="0 0 580 885" width="580" height="885" aria-hidden="true">
      <defs>
        <linearGradient id="paper" x1="0" y1="0" x2="1" y2="1">
          <stop offset="0" stop-color="#fbfbfc"/>
          <stop offset="0.5" stop-color="var(--label-paper)"/>
          <stop offset="1" stop-color="var(--marble-vein)"/>
        </linearGradient>
      </defs>
      <path class="frame-outer"
            d="M26 96 H166 V88 C166 20 206 8 288 8 C370 8 410 20 410 88 V96 H554 Q568 96 568 110 V862 Q568 876 554 876 H26 Q12 876 12 862 V110 Q12 96 26 96 Z"
            fill="url(#paper)" stroke="#ffffff" stroke-width="10"/>
      <path class="frame-band"
            d="M30 106 H176 V90 C176 32 212 20 288 20 C364 20 400 32 400 90 V106 H550 V866 H30 Z"
            fill="none" stroke="var(--frame-grey)" stroke-width="12"/>
      <path class="frame-fine"
            d="M46 120 H188 V96 C188 46 220 36 288 36 C356 36 388 46 388 96 V120 H534 V850 H46 Z"
            fill="none" stroke="var(--frame-light)" stroke-width="2"/>
      <rect class="inner-panel" x="68" y="340" width="444" height="496" fill="none" stroke="var(--frame-light)" stroke-width="4"/>
      <g class="title-stripes" fill="var(--frame-light)">
        <rect x="30" y="236" width="98" height="5"/>
        <rect x="30" y="258" width="98" height="5"/>
        <rect x="30" y="282" width="98" height="5"/>
        <rect x="30" y="306" width="98" height="5"/>
        <rect x="452" y="236" width="98" height="5"/>
        <rect x="452" y="258" width="98" height="5"/>
        <rect x="452" y="282" width="98" height="5"/>
        <rect x="452" y="306" width="98" height="5"/>
      </g>
    </svg>

    <div class="brand-row">
      <h1 class="brand-name">KOLVAT</h1>
    </div>

    <div class="fruit-art" role="img" aria-label="Photograph of ripe red mulberries on green mulberry leaves"></div>

    <div class="content-band">
      <p class="content-claim">100% MULBERRY</p>
    </div>
  </main>
</body>
</html>
```